skin elixir serum with snail extract

I am working at a natural skincare company. We are going to launch a new product - a skin serum. completely natural, super concentrated, multi use (face, neck , eyes). But we need the packaging (box and bottle label) to be aligned to our brand's philosophy, design etc. (See more at dovrenta.com)

Here's a more detailed description :
"Elevate your skincare routine with BrimZest Tonic, the ultimate one-drop wonder enriched with potent snail secretion. Experience the magic as our 100% natural serum transforms your face, eyes, décolleté, and neck. Get ready to say Wow to a new level of radiance!"

Target Market(s)

natural skincare enthusiasts - beauty pioneers

Industry/Entity Type

beauty - wellness

Requirements
Nice to have
• based on the overall brand philosophy (see dovrenta.com)

```html
<!DOCTYPE html>
<html lang="en">
<head>
<meta charset="utf-8">
<title>dovrenta – Skin Elixir Serum packaging</title>
<link rel="stylesheet" href="https://fonts.googleapis.com/css2?family=Poppins:wght@400;500;600&display=swap">
<style>
  :root {
    --backdrop: #808080;
    --board: #f3f3f3;
    --board-edge: #c9c9c9;
    --plum: #7b0042;
    --white: #ffffff;
  }
  * { box-sizing: border-box; margin: 0; padding: 0; }
  html, body { width: 1200px; height: 903px; overflow: hidden; background: var(--backdrop); }
  .canvas { position: relative; width: 1200px; height: 903px; font-family: "Poppins", Arial, sans-serif; }
  .dieline { position: absolute; left: 0; top: 0; }

  .panel { position: absolute; top: 283px; height: 345px; }
  .panel--info { background: var(--plum); color: var(--white); width: 150px; padding: 27px 8px 0 12px; font-size: 8.4px; line-height: 12px; font-weight: 500; }
  .panel--info p { margin-bottom: 10px; }
  .panel--info .strong { font-weight: 600; }
  .panel--info .gap { margin-top: 20px; }
  .panel--info .gap-lg { margin-top: 16px; }
  .panel--front { background: var(--white); width: 146px; text-align: center; color: var(--plum); }

  .brand { position: absolute; width: 150px; text-align: center; font-family: "Poppins", Arial, sans-serif; font-weight: 500; font-size: 22px; line-height: 26px; color: var(--plum); }

  .front-copy { position: absolute; left: 0; width: 100%; text-align: center; color: var(--plum); font-weight: 500; }
  .product-name { font-size: 10.5px; line-height: 15px; }
  .zones { font-size: 7.6px; letter-spacing: 0.6px; }
  .claims { font-size: 7px; line-height: 9.5px; }
  .volume { font-size: 7px; line-height: 11px; }
  .volume b { font-weight: 600; }

  .label { position: absolute; left: 910px; top: 306px; width: 103px; height: 315px; background: var(--white); border: 1px solid var(--board-edge); border-radius: 0 0 12px 12px; overflow: hidden; }
  .label__band { height: 119px; background: var(--plum); }
  .label .brand { width: 101px; left: 0; top: 135px; font-size: 17px; line-height: 20px; }
  .label .product-name { font-size: 8px; line-height: 11px; }
  .label .zones { font-size: 5.6px; }
  .label .claims { font-size: 5.2px; line-height: 7px; }
  .label .volume { font-size: 5.2px; line-height: 9px; }
</style>
</head>
<body>
<main class="canvas">
  <svg class="dieline" width="1200" height="903" viewBox="0 0 1200 903" role="img" aria-label="Folding carton dieline with a faint grey line-art botanical pattern across the board">
    <path d="M191,283 L258,250 L258,172 L300,172 L381,245 L381,85 Q381,75 391,75 L522,75 Q532,75 532,85 L532,172 L575,172 L655,245 L655,283 L828,283 L828,825 Q828,835 818,835 L690,835 Q680,835 680,825 L680,628 L655,628 L655,742 L536,742 L536,645 L381,645 L381,742 L258,742 L258,700 L191,640 Z"
          fill="var(--board)" stroke="var(--board-edge)" stroke-width="2"/>
  </svg>

  <section class="panel panel--info" style="left:234px">
    <p>Lorem Ipsum is simply dummy text of the printing and typesetting industry. Lorem Ipsum has been the industry's standard dummy text ever since the 1500s</p>
    <p class="strong">Lorem Ipsum is simply dummy text of the printing and typesetting industry.</p>
    <p class="gap">Lorem Ipsum is simply dummy text of the printing and typesetting industry. Lorem Ipsum has been the industry's standard dummy text ever since the 1500s</p>
    <p class="strong gap">Lorem Ipsum is simply dummy text of the printing</p>
    <p class="strong gap-lg">dummy text of the printing</p>
  </section>

  <section class="panel panel--front" style="left:384px">
    <div class="brand" style="left:-2px; top:98px;">dovrenta</div>
    <div class="front-copy" style="top:180px"><p class="product-name">SKIN<br>ELIXIR SERUM</p></div>
    <div class="front-copy" style="top:226px"><p class="zones">FACE | NECK | EYE</p></div>
    <div class="front-copy" style="top:252px"><p class="claims">completely natural, super<br>concentrated, multi use</p></div>
    <div class="front-copy" style="top:293px"><p class="volume">Natural Serum<br><b>30ml</b></p></div>
  </section>

  <section class="panel panel--info" style="left:530px">
    <p>Lorem Ipsum is simply dummy text of the printing and typesetting industry. Lorem Ipsum has been the industry's standard dummy text ever since the 1500s</p>
    <p class="strong">Lorem Ipsum is simply dummy text of the printing and typesetting industry.</p>
    <p class="gap">Lorem Ipsum is simply dummy text of the printing and typesetting industry. Lorem Ipsum has been the industry's standard dummy text ever since the 1500s</p>
    <p class="strong gap">Lorem Ipsum is simply dummy text of the printing</p>
    <p class="strong gap-lg">dummy text of the printing</p>
  </section>

  <div class="brand" style="left:680px; top:444px;">dovrenta</div>
  <div class="brand" style="left:381px; top:168px;">dovrenta</div>

  <aside class="label">
    <div class="label__band"></div>
    <div class="brand">dovrenta</div>
    <div class="front-copy" style="top:199px"><p class="product-name">SKIN<br>ELIXIR SERUM</p></div>
    <div class="front-copy" style="top:233px"><p class="zones">FACE | NECK | EYE</p></div>
    <div class="front-copy" style="top:252px"><p class="claims">completely natural, super<br>concentrated, multi use</p></div>
    <div class="front-copy" style="top:284px"><p class="volume">Natural Serum<br><b>30ml</b></p></div>
  </aside>
</main>
</body>
</html>
```